CD Design Cover - "Beyond The Quiet Fields"

I need a CD cover design. The original Album or CD was recorded in the early eighties. We are re-mastering it. It needs a fresh cover. The genre' is contemporary Christian music and the title of the album is "Beyond The Quiet Fields." This is referring to caring outside of the church walls. A picture of the solo artist could be integrated in the back design. It is not a good picture and does not have to be used. You would have to be creative in using it because of the quality. It does not have to be used at all. I also added some pictures I liked that could be used. I think I like the "Empty church opening" the best. Fits the theme perfectly.

Target Market(s)

30 years old and older.

Requirements
Must have
• Warmth
Nice to have
• I attached two pictures. One of an empty church and one with a reflection of a stain glass window on the wall. It would be nice to see some offerings using these pictures.
Should not have
• Not too churchy

```html
<!DOCTYPE html>
<html lang="en">
<head>
<meta charset="utf-8">
<title>Beyond The Quiet Fields – Dan Hollister</title>
<link rel="stylesheet" href="https://fonts.googleapis.com/css2?family=Allura&family=Nothing+You+Could+Do&family=Open+Sans:wght@300;400&display=swap">
<style>
  :root {
    --backdrop: #9e9d96;
    --ochre: #b57c2c;
    --ochre-deep: #9a5a1f;
    --rust: #8a3f1a;
    --night: #141c26;
    --teal: #1f3a40;
    --moss: #4a5a3a;
    --wood: #3a2e22;
    --glow: #fbe27a;
    --sun: #f3b53a;
    --meadow: #c8b23a;
    --ink-light: #f4efe4;
    --skin: #c99a7a;
  }
  * { box-sizing: border-box; margin: 0; padding: 0; }
  html, body { width: 1200px; height: 1200px; overflow: hidden; background: var(--backdrop); }
  .stage { position: relative; width: 1200px; height: 1200px; overflow: hidden; }

  .sleeve { position: absolute; left: 32px; top: 158px; width: 1142px; height: 502px; display: flex;
    box-shadow: 0 8px 14px rgba(0,0,0,.25); }

  /* back panel */
  .back {
    position: relative; width: 560px; height: 100%;
    background:
      radial-gradient(ellipse at 70% 85%, rgba(138,63,26,.55), transparent 60%),
      radial-gradient(ellipse at 30% 20%, rgba(214,150,60,.45), transparent 65%),
      linear-gradient(180deg, var(--ochre) 0%, #a8692a 60%, var(--ochre-deep) 100%);
    color: var(--ink-light);
  }
  .artist-portrait { position: absolute; left: 42px; top: 24px; width: 62px; height: 94px; border-radius: 45%;
    background: radial-gradient(ellipse, var(--skin) 40%, rgba(201,154,122,0) 75%); }
  .tracklist { position: absolute; left: 146px; top: 122px; width: 220px; list-style: none; text-align: center;
    font-family: "Nothing You Could Do", cursive; font-size: 13px; line-height: 18.4px; white-space: nowrap; }
  .label-block { position: absolute; left: 416px; top: 390px; width: 120px; text-align: center;
    font-family: "Open Sans", sans-serif; font-size: 7px; letter-spacing: .08em; line-height: 9px; }
  .label-name { text-transform: uppercase; }
  .credits { position: absolute; left: 160px; top: 444px; width: 200px; text-align: center;
    font-family: "Open Sans", sans-serif; font-size: 6.5px; letter-spacing: .08em; line-height: 8px; }
  .imprint { position: absolute; left: 22px; top: 444px; display: flex; align-items: center; gap: 5px;
    font-family: "Open Sans", sans-serif; font-size: 9px; font-weight: 400; color: var(--ink-light); }
  .imprint-dot { width: 12px; height: 12px; border-radius: 50%; background: var(--sun); }

  /* spine */
  .spine { position: relative; width: 24px; height: 100%; background: linear-gradient(180deg, var(--teal), var(--night)); color: var(--ink-light); }
  .spine-mark { position: absolute; top: 8px; left: 6px; width: 12px; height: 12px; border-radius: 50%; background: var(--ochre); }
  .spine-text { position: absolute; top: 190px; left: 3px; writing-mode: vertical-rl; display: flex; gap: 26px; align-items: center; }
  .spine-artist { font-family: "Open Sans", sans-serif; font-weight: 300; font-size: 11px; letter-spacing: .12em; }
  .spine-title { font-family: "Allura", cursive; font-size: 13px; }

  /* front */
  .front { position: relative; width: 558px; height: 100%; overflow: hidden; color: var(--ink-light); }
  .cover-art { position: absolute; inset: 0;
    background:
      radial-gradient(ellipse 20% 30% at 56% 42%, var(--glow) 0%, var(--sun) 40%, rgba(243,181,58,0) 100%),
      radial-gradient(ellipse 28% 42% at 56% 55%, rgba(200,178,58,.9) 0%, rgba(150,130,50,.55) 55%, rgba(74,90,58,0) 100%),
      radial-gradient(ellipse 18% 26% at 10% 35%, rgba(170,220,200,.35), transparent 100%),
      radial-gradient(ellipse 18% 26% at 94% 35%, rgba(170,220,200,.35), transparent 100%),
      linear-gradient(180deg, var(--night) 0%, var(--teal) 40%, var(--moss) 62%, var(--wood) 100%); }
  .artist-name { position: absolute; top: 46px; width: 100%; text-align: center;
    font-family: "Open Sans", sans-serif; font-weight: 400; font-size: 21px; letter-spacing: .1em; }
  .album-title { position: absolute; top: 402px; width: 100%; text-align: center; font-weight: 400;
    font-family: "Allura", cursive; font-size: 46px; white-space: nowrap; }

  /* disc */
  .disc { position: absolute; left: 466px; top: 656px; width: 488px; height: 488px; border-radius: 50%; background: #0c0c0c; overflow: hidden; color: var(--ink-light); }
  .disc-art { position: absolute; inset: 30px; border-radius: 50%;
    background:
      radial-gradient(ellipse 22% 30% at 52% 32%, var(--glow) 0%, var(--sun) 40%, rgba(243,181,58,0) 100%),
      radial-gradient(ellipse 32% 46% at 52% 50%, rgba(200,178,58,.9) 0%, rgba(150,130,50,.5) 55%, rgba(74,90,58,0) 100%),
      linear-gradient(180deg, var(--night) 0%, var(--teal) 40%, var(--moss) 62%, var(--wood) 100%); }
  .disc-hole { position: absolute; left: 208px; top: 208px; width: 72px; height: 72px; border-radius: 50%; background: var(--backdrop); box-shadow: 0 0 0 3px #b9bcc0; }
  .disc-artist { position: absolute; top: 20px; width: 100%; text-align: center;
    font-family: "Open Sans", sans-serif; font-size: 14px; letter-spacing: .1em; }
  .disc-title { position: absolute; top: 350px; width: 100%; text-align: center;
    font-family: "Allura", cursive; font-size: 30px; white-space: nowrap; }
  .disc-label { position: absolute; left: 360px; top: 200px; width: 100px; text-align: center;
    font-family: "Open Sans", sans-serif; font-size: 6px; letter-spacing: .08em; line-height: 7.5px; }
</style>
</head>
<body>
<main class="stage">
  <section class="sleeve">
    <div class="back">
      <div class="artist-portrait" role="img" aria-label="Portrait photo of the artist"></div>
      <ol class="tracklist">
        <li>Special Delivery</li>
        <li>Beyond The Quiet Fields</li>
        <li>Ordinary People</li>
        <li>The Day He Wore My Crown</li>
        <li>He's Alive</li>
        <li>One More Song for You</li>
        <li>The Lord's Prayer</li>
        <li>Home Where I Belong</li>
        <li>How Great Thou Art</li>
        <li>We Shall Behold Him</li>
      </ol>
      <div class="label-block">
        <p class="label-name">Meadowlark Records</p>
        <p>Briar Hill, MO 65012</p>
      </div>
      <div class="imprint"><span class="imprint-dot"></span><span>Meadowlark Records</span></div>
      <div class="credits">
        <p>Producer: Nora Ellis</p>
        <p>Engineered: Paul Kessler</p>
        <p>Recorded at: Meadowlark Studio</p>
        <p>Promoter: Ray Dunn</p>
      </div>
    </div>

    <div class="spine">
      <span class="spine-mark"></span>
      <div class="spine-text">
        <span class="spine-artist">Dan Hollister</span>
        <span class="spine-title">Beyond The Quiet Fields</span>
      </div>
    </div>

    <div class="front">
      <div class="cover-art" role="img" aria-label="Empty wooden church with pews and side windows; the far wall opens like a rock cave onto a sunlit golden meadow"></div>
      <h2 class="artist-name">Dan Hollister</h2>
      <h1 class="album-title">Beyond The Quiet Fields</h1>
    </div>
  </section>

  <section class="disc">
    <div class="disc-art" role="img" aria-label="Church interior opening onto a sunlit golden meadow"></div>
    <p class="disc-artist">Dan Hollister</p>
    <p class="disc-label">MEADOWLARK RECORDS<br>Briar Hill, MO 65012</p>
    <p class="disc-title">Beyond The Quiet Fields</p>
    <span class="disc-hole"></span>
  </section>
</main>
</body>
</html>
```